Design a Future- POV DKVANTOM

Refresh the images/Theme. Focus theme/images on the following

1. Adaptability
2. Resilience
3. Emotional Inteligence
4. Relentless execution
5. High Care Factor

Industry/Entity Type

Technology Equipment

Font styles to use
Other font styles liked:
• Norvex Sans

Colors
33a6d7
cfdeed
85acd3
85cae6
fcf7c1
3377b5
fee18a

Requirements
Must have
• Consistent theme
Professional almost marketing look and feel
Nice to have
• none
Should not have
• none

```html
<!DOCTYPE html>
<html lang="en">
<head>
<meta charset="utf-8">
<title>Future POV – DK Vantom</title>
<link href="https://fonts.googleapis.com/css2?family=Montserrat:wght@400;500;600;700;800&family=Open+Sans:wght@400;600;700&display=swap" rel="stylesheet">
<style>
:root{
  --navy:#0c2e66;
  --navy-2:#173f80;
  --blue:#33a6d7;
  --blue-2:#3377b5;
  --sky:#85cae6;
  --mist:#cfdeed;
  --steel:#85acd3;
  --cream:#fcf7c1;
  --gold:#fee18a;
  --ink:#1d2733;
  --grey:#6b7787;
  --canvas:#e4e8ee;
}
*{box-sizing:border-box;margin:0;padding:0}
html,body{width:764px;height:1200px;overflow:hidden}
body{background:var(--canvas);font-family:"Open Sans",sans-serif;color:var(--ink);position:relative}
.sprite{position:absolute;width:0;height:0;overflow:hidden}
.hero{position:absolute;left:0;top:0;width:764px;height:316px;overflow:hidden}
.hero-photo{position:absolute;inset:0;background:linear-gradient(100deg,#b9bec6 0%,#cfc7bb 28%,#dedad3 50%,var(--canvas) 70%)}
.hero-title{position:absolute;left:44px;top:118px;font-family:Montserrat,sans-serif;line-height:.98}
.hero-title .word-a{display:block;font-size:39px;font-weight:800;color:#1a8fe0;letter-spacing:-.5px}
.hero-title .word-b{display:block;font-size:39px;font-weight:400;color:#1b1b1b;padding-left:81px}
.hero-slide{position:absolute;left:357px;top:55px;width:300px;height:167px;overflow:hidden;box-shadow:0 6px 18px rgba(20,40,70,.25)}
.deck{position:absolute;left:9px;top:318px;display:grid;grid-template-columns:repeat(3,244px);grid-auto-rows:137px;column-gap:7.5px;row-gap:9.5px}
.slide{position:relative;overflow:hidden;background:#fff;font-size:4px;line-height:1.25}
.abs{position:absolute}
.photo-city{background:linear-gradient(180deg,#e3ebf3 0%,#d3dce6 40%,#a4afbd 70%,#6f7a8a 100%)}
.title{font-family:Montserrat,sans-serif;color:var(--navy);font-weight:600}
.cover-title{font-family:Montserrat,sans-serif;font-weight:600;color:var(--navy)}
.spaced{letter-spacing:2px;font-size:5px}
.page{position:absolute;right:5px;bottom:4px;display:flex;align-items:center;gap:3px;font-size:2.6px;letter-spacing:1px;color:#9aa}
.page i{display:inline-block;width:7px;height:7px;border-radius:50%;background:var(--blue);color:#fff;font-style:normal;font-size:3px;text-align:center;line-height:7px;letter-spacing:0}
.ic{position:absolute;display:flex;align-items:center;justify-content:center;border-radius:50%;background:var(--blue);border:1.5px solid #fff;box-shadow:0 0 0 1px var(--mist);color:#fff}
.ic svg{width:58%;height:58%}
.ic.static{position:relative}
.col-card{position:absolute;background:#fff;box-shadow:0 2px 6px rgba(12,46,102,.15);text-align:center;border-bottom:2px solid var(--gold)}
.col-card .head{background:var(--navy);color:#fff;font-weight:700;font-size:5px;height:24px;padding-top:7px}
.col-card .ic{position:relative;width:20px;height:20px;margin:-9px auto 3px}
.col-card p{font-size:3.7px;color:var(--ink)}
.col-card p.hl{color:var(--blue)}
.bullets li{list-style:none;position:relative;padding-left:5px;margin-bottom:1.5px}
.bullets li::before{content:"";position:absolute;left:0;top:.9px;border-left:2px solid var(--blue);border-top:1.2px solid transparent;border-bottom:1.2px solid transparent}
.tag{position:absolute;font-size:4px;font-weight:700;color:#fff;padding:1px 3px}
.award{width:22px;height:20px;border-radius:50%;background:radial-gradient(circle,#fffbe4 45%,#f3e6b4 100%);border:1px solid #dccb8e}
.num{position:absolute;width:12px;height:12px;border-radius:50%;background:var(--blue);border:1.2px solid #fff;box-shadow:0 0 0 1px var(--mist);color:#fff;font-size:3.5px;text-align:center;line-height:10px;font-weight:700}
.exp-card{position:absolute;background:#fff;box-shadow:0 2px 6px rgba(12,46,102,.15);border-bottom:2px solid var(--blue)}
.exp-card .rule{position:absolute;left:5px;top:2px;width:18px;height:1.5px;background:var(--blue)}
.year{position:absolute;width:18px;height:18px;border-radius:50%;background:var(--blue);border:1.5px solid #fff;box-shadow:0 0 0 1px var(--mist);color:#fff;font-size:3.8px;text-align:center;line-height:15px;font-weight:700}
.cap{position:absolute;text-align:center;font-size:2.8px;line-height:1.25}
</style>
</head>
<body>

<svg class="sprite" aria-hidden="true">
  <symbol id="i-user" viewBox="0 0 24 24"><g fill="none" stroke="currentColor" stroke-width="2"><circle cx="12" cy="8" r="4"/><path d="M4 21c0-4 4-7 8-7s8 3 8 7"/></g></symbol>
  <symbol id="i-users" viewBox="0 0 24 24"><g fill="none" stroke="currentColor" stroke-width="2"><circle cx="9" cy="8" r="3.2"/><circle cx="16.5" cy="9" r="2.6"/><path d="M3 20c0-3.5 2.8-6 6-6s6 2.5 6 6M15 14.5c3 0 6 2 6 5"/></g></symbol>
  <symbol id="i-list" viewBox="0 0 24 24"><g fill="none" stroke="currentColor" stroke-width="2"><rect x="5" y="3" width="14" height="18" rx="2"/><path d="M9 8h6M9 12h6M9 16h4"/></g></symbol>
  <symbol id="i-gear" viewBox="0 0 24 24"><g fill="none" stroke="currentColor" stroke-width="2"><circle cx="12" cy="12" r="3.5"/><path d="M12 2v3M12 19v3M2 12h3M19 12h3M4.9 4.9l2.1 2.1M17 17l2.1 2.1M4.9 19.1L7 17M17 7l2.1-2.1"/></g></symbol>
  <symbol id="i-target" viewBox="0 0 24 24"><g fill="none" stroke="currentColor" stroke-width="2"><circle cx="11" cy="13" r="8"/><circle cx="11" cy="13" r="4"/><path d="M11 13l9-9M16 4h4v4"/></g></symbol>
  <symbol id="i-search" viewBox="0 0 24 24"><g fill="none" stroke="currentColor" stroke-width="2.2"><circle cx="10" cy="10" r="6.5"/><path d="M15 15l6 6"/></g></symbol>
  <symbol id="i-bulb" viewBox="0 0 24 24"><g fill="none" stroke="currentColor" stroke-width="2"><path d="M9 17h6M10 21h4M12 3a6 6 0 0 0-4 10.5c1 1 1 2 1 3.5h6c0-1.5 0-2.5 1-3.5A6 6 0 0 0 12 3z"/></g></symbol>
  <symbol id="i-chart" viewBox="0 0 24 24"><g fill="none" stroke="currentColor" stroke-width="2"><path d="M4 20h16M7 20v-5M12 20v-8M17 20v-11M5 11l5-4 3 2 6-5"/></g></symbol>
  <symbol id="i-eye" viewBox="0 0 24 24"><g fill="none" stroke="currentColor" stroke-width="2"><circle cx="7" cy="15" r="4"/><circle cx="17" cy="15" r="4"/><path d="M11 15h2M5 11l2-6h3l1 5M19 11l-2-6h-3l-1 5"/></g></symbol>
  <symbol id="i-cycle" viewBox="0 0 24 24"><g fill="none" stroke="currentColor" stroke-width="2"><path d="M20 12a8 8 0 0 1-14 5.3M4 12a8 8 0 0 1 14-5.3"/><path d="M18 3v4h-4M6 21v-4h4"/></g></symbol>
  <symbol id="i-hand" viewBox="0 0 24 24"><g fill="none" stroke="currentColor" stroke-width="2"><path d="M3 12l4-4 4 2 3-2 4 1 3 3-6 6-5-3M7 8l7 7"/></g></symbol>
  <symbol id="i-quote" viewBox="0 0 24 24"><path fill="currentColor" d="M4 18v-5c0-4 2-7 6-8v3c-2 .8-3 2.2-3 4h3v6H4zm10 0v-5c0-4 2-7 6-8v3c-2 .8-3 2.2-3 4h3v6h-6z"/></symbol>
  <symbol id="i-arrow" viewBox="0 0 24 24"><g fill="none" stroke="currentColor" stroke-width="2.4"><circle cx="12" cy="12" r="9"/><path d="M10 8l4 4-4 4"/></g></symbol>
</svg>

<section class="hero">
  <div class="hero-photo" role="img" aria-label="Sunset photograph of a crowd with raised hands"></div>
  <h1 class="hero-title"><span class="word-a">Presentation</span><span class="word-b">Deck</span></h1>
  <div class="hero-slide">
    <div class="abs photo-city" style="inset:0" role="img" aria-label="Hazy city skyline photograph"></div>
    <div class="abs" style="left:0;right:0;top:68px;text-align:center">
      <div class="cover-title" style="font-size:21px;line-height:1">New Role</div>
      <div style="font-size:8px;color:var(--navy)">Point of View Document</div>
    </div>
    <div class="abs" style="left:0;right:0;top:146px;text-align:center;color:var(--navy)">
      <div class="spaced">DK VANTOM</div>
      <div style="font-size:5px">Month 2020</div>
    </div>
  </div>
</section>

<main class="deck">

  <article class="slide">
    <div class="abs photo-city" style="inset:0" role="img" aria-label="City skyline photograph"></div>
    <div class="abs" style="left:82px;top:56px;text-align:center">
      <div class="cover-title" style="font-size:16px;line-height:1">New Role</div>
      <div style="font-size:6.5px;color:var(--navy)">Point of View Document</div>
    </div>
    <div class="abs" style="left:95px;top:118px;text-align:center;color:var(--navy)">
      <div class="spaced" style="font-size:4.5px">DK VANTOM</div>
      <div style="font-size:4px">Month 2020</div>
    </div>
  </article>

  <article class="slide">
    <div class="abs" style="left:0;right:0;top:0;height:99px;background:linear-gradient(180deg,#eef2f7,#dde5ee)" role="img" aria-label="Faint city skyline photograph"></div>
    <div class="abs" style="left:0;right:0;top:47px;text-align:center">
      <div class="cover-title" style="font-size:15px;line-height:1">New Role</div>
      <div style="font-size:5.5px;letter-spacing:1px;color:var(--grey)">POINT OF VIEW DOCUMENT</div>
    </div>
    <div class="abs" style="left:0;right:0;bottom:0;height:38px;background:var(--navy);color:#fff;text-align:center;padding-top:14px">
      <div class="spaced" style="font-size:4.5px">DK VANTOM</div>
      <div style="font-size:4px;font-weight:700">Month 2020</div>
    </div>
  </article>

  <article class="slide" style="background:var(--mist)">
    <svg class="abs" style="inset:0" width="244" height="137" viewBox="0 0 244 137">
      <polygon points="0,0 155,0 72,137 0,137" fill="var(--navy-2)"/>
    </svg>
    <div class="abs" style="left:15px;top:60px;color:#fff;font-family:Montserrat,sans-serif;font-weight:600;font-size:11px">Table of Content</div>
    <ol class="abs" style="left:112px;top:28px;list-style:none;font-size:4.5px;color:var(--ink);line-height:16px">
      <li style="padding-left:42px"><b>01</b> About Me</li>
      <li style="padding-left:34px"><b>02</b> Leadership Philosophy</li>
      <li style="padding-left:26px"><b>03</b> Qualifications</li>
      <li style="padding-left:18px"><b>04</b> 30-60-90 Day Plan</li>
      <li style="padding-left:10px"><b>05</b> FY19 Success Defined</li>
      <li style="padding-left:2px"><b>06</b> Sponsors</li>
    </ol>
  </article>

  <article class="slide">
    <div class="abs" style="left:0;width:104px;top:8px;text-align:center">
      <div class="title" style="font-size:12px;line-height:1.1">My<br>“What Matters?”</div>
    </div>
    <svg class="abs" style="left:12px;top:42px" width="84" height="86" viewBox="0 0 84 86">
      <path d="M42 2 Q46 2 50 4 L78 20 Q82 22 82 27 L82 59 Q82 64 78 66 L50 82 Q46 84 42 84 Q38 84 34 82 L6 66 Q2 64 2 59 L2 27 Q2 22 6 20 L34 4 Q38 2 42 2Z" fill="#1a9be0"/>
    </svg>
    <div class="abs" style="left:14px;top:65px;width:80px;text-align:center;color:#fff;font-size:6px;line-height:1.3">Servant Leadership<br>“Why We CAN”<br>Mindset Culture by<br>Design Golden Rule<br>Be Present</div>
    <div class="abs" style="left:104px;top:0;right:0;bottom:0;background:linear-gradient(160deg,#5b5550 0%,#8f7f78 30%,#9c5a5a 50%,#3d4466 72%,#7c8fae 100%)" role="img" aria-label="Collage of team event and volunteering photographs"></div>
  </article>

  <article class="slide">
    <div class="abs" style="left:0;right:0;top:0;height:73px;background:linear-gradient(120deg,#123a78,#0c2e66)"></div>
    <div class="abs" style="left:0;right:0;top:8px;text-align:center;color:#fff;font-family:Montserrat,sans-serif;font-weight:600;font-size:10px">Leadership Philosophy</div>
    <span class="ic" style="left:116px;top:25px;width:12px;height:12px"><svg><use href="#i-quote"/></svg></span>
    <div class="abs" style="left:22px;right:22px;top:41px;text-align:center;color:#fff;font-size:3.5px">“ Great leaders are almost always great simplifiers, who can cut through argument, debate and doubt to offer a solution everybody can understand.”</div>
    <div class="abs" style="left:0;right:0;top:60px;text-align:center;color:#cdd;font-size:3px;font-style:italic">– Gen. Arden Hale, former Secretary of State</div>
    <div class="abs" style="left:12px;top:84px;font-size:4.5px;font-weight:700;color:var(--navy)">My formula for success has been:</div>
    <ul class="abs" style="left:12px;top:93px;font-size:3.6px;color:var(--grey);line-height:9px;list-style:none">
      <li><svg width="5" height="5" style="color:var(--blue);vertical-align:-1px"><use href="#i-arrow"/></svg> Hiring great leaders</li>
      <li><svg width="5" height="5" style="color:var(--blue);vertical-align:-1px"><use href="#i-arrow"/></svg> Over communicating the stretch vision</li>
      <li><svg width="5" height="5" style="color:var(--blue);vertical-align:-1px"><use href="#i-arrow"/></svg> Making good, data-driven decisions</li>
      <li><svg width="5" height="5" style="color:var(--blue);vertical-align:-1px"><use href="#i-arrow"/></svg> Finding ways to scale it</li>
    </ul>
    <div class="abs" style="left:145px;top:84px;font-size:5.5px;font-weight:700;color:var(--navy)">Key Capabilities</div>
    <div class="abs" style="left:112px;top:97px;display:flex;gap:12px;font-size:3.8px;text-align:center">
      <div style="width:20px"><span class="ic static" style="width:16px;height:16px;margin:0 auto 3px"><svg><use href="#i-bulb"/></svg></span>Sense-making</div>
      <div style="width:20px"><span class="ic static" style="width:16px;height:16px;margin:0 auto 3px"><svg><use href="#i-hand"/></svg></span>Relating</div>
      <div style="width:20px"><span class="ic static" style="width:16px;height:16px;margin:0 auto 3px"><svg><use href="#i-target"/></svg></span>Visioning</div>
      <div style="width:20px"><span class="ic static" style="width:16px;height:16px;margin:0 auto 3px"><svg><use href="#i-gear"/></svg></span>Inventing</div>
    </div>
  </article>

  <article class="slide">
    <div class="abs" style="left:10px;top:8px;display:flex;flex-direction:column;gap:5px" role="img" aria-label="Column of award badges">
      <div class="award"></div><div class="award"></div><div class="award"></div><div class="award"></div><div class="award"></div>
    </div>
    <div class="abs title" style="left:51px;top:44px;font-size:11px;line-height:1.1">Why Me &amp;<br>Why This<br>Role</div>
    <div class="abs" style="left:51px;top:83px;font-size:4px;font-weight:700;color:var(--blue-2)">EXECUTE FOR RESULTS,<br>CARE FOR CULTURE</div>
    <span class="ic" style="left:128px;top:16px;width:20px;height:20px"><svg><use href="#i-search"/></svg></span>
    <div class="abs" style="left:154px;top:15px;width:86px;font-size:3.4px;color:var(--blue)"><b style="font-size:4.3px">Track record of Success &amp; Leadership</b>
      <ul class="bullets" style="margin-top:3px"><li>History of exceeding growth targets</li><li>Selected for leadership programs</li><li>Proven adaptability</li></ul></div>
    <span class="ic" style="left:128px;top:57px;width:20px;height:20px;background:var(--blue-2)"><svg><use href="#i-users"/></svg></span>
    <div class="abs" style="left:154px;top:57px;width:86px;font-size:3.4px;color:var(--blue-2)"><b style="font-size:4.3px">Diverse Industry &amp; Role Experience</b>
      <ul class="bullets" style="margin-top:3px"><li>Software &amp; CX background</li><li>IT Services Sales</li><li>Refugee Operations abroad</li></ul></div>
    <span class="ic" style="left:128px;top:97px;width:20px;height:20px;background:var(--sky)"><svg><use href="#i-user"/></svg></span>
    <div class="abs" style="left:154px;top:97px;width:86px;font-size:3.4px;color:var(--sky)"><b style="font-size:4.3px">Think Big &amp; Act Small</b>
      <ul class="bullets" style="margin-top:3px"><li>Culture builder</li><li>Model Optimization</li><li>Program Development &amp; Execution</li></ul></div>
    <div class="page">PAGE <i>6</i></div>
  </article>

  <article class="slide" style="background:linear-gradient(180deg,#fff,#f1f4f8)">
    <div class="abs title" style="left:0;right:0;top:14px;text-align:center;font-size:13px;font-weight:400">30-60-90 Day Plan</div>
    <div class="col-card" style="left:20px;top:42px;width:61px;height:74px"><div class="head">People</div><span class="ic"><svg><use href="#i-user"/></svg></span>
      <p>Build Trust</p><p class="hl">Market Visits – Town Hall</p><p>Leadership Team</p><p class="hl">Direct Teams</p><p>Engineering Team</p><p class="hl">Dotted line resources</p></div>
    <div class="col-card" style="left:95px;top:42px;width:61px;height:74px"><div class="head">Pipeline</div><span class="ic"><svg><use href="#i-list"/></svg></span>
      <p>90 day Pipeline</p><p class="hl">Key Deals</p><p>Qtr Event Calendar</p><p class="hl">Portfolio Balance</p><p>2X2</p></div>
    <div class="col-card" style="left:168px;top:42px;width:61px;height:74px"><div class="head">Process</div><span class="ic"><svg><use href="#i-gear"/></svg></span>
      <p>Team Cadence</p><p class="hl">Top | Down expectations</p><p>Bottom | Up expectations</p><p class="hl">Forecast Methodology</p><p>Reporting Packages</p><p class="hl">Old vs. Now</p></div>
    <div class="page">PAGE <i>7</i></div>
  </article>

  <article class="slide" style="background:linear-gradient(180deg,#fff,#f1f4f8)">
    <div class="abs title" style="left:0;right:0;top:4px;text-align:center;font-size:13px;font-weight:400">30-60-90 Day Plan</div>
    <div class="col-card" style="left:20px;top:42px;width:61px;height:74px"><div class="head">People</div><span class="ic"><svg><use href="#i-user"/></svg></span>
      <p>Build Trust</p><p class="hl">Market Visits – Town Hall</p><p>Leadership Team</p><p class="hl">Direct Teams</p><p>Engineering Team</p><p class="hl">Dotted line resources</p></div>
    <div class="col-card" style="left:168px;top:42px;width:61px;height:74px"><div class="head">Process</div><span class="ic"><svg><use href="#i-gear"/></svg></span>
      <p>Team Cadence</p><p class="hl">Top | Down expectations</p><p>Bottom | Up expectations</p><p class="hl">Forecast Methodology</p><p>Reporting Packages</p><p class="hl">Old vs. Now</p></div>
    <div class="col-card" style="left:77px;top:22px;width:92px;height:111px">
      <div class="head" style="height:38px;font-size:6.5px;padding-top:10px">90 day Goals</div>
      <span class="ic" style="width:30px;height:30px;margin-top:-14px"><svg><use href="#i-target"/></svg></span>
      <p style="font-size:4.2px">1. Transition in rear view mirror</p><p class="hl" style="font-size:4.2px">2. Rhythm/Cadence in place</p><p style="font-size:4.2px">3. Hit Plan in current Qtr</p><p class="hl" style="font-size:4.2px">4. Leadership engagement w/:</p><p style="font-size:2.8px">Top 15 Customers | Prospects</p><p style="font-size:4.2px">5. Pipeline supports next Qtr</p><p class="hl" style="font-size:4.2px">6. Hire Key Roles</p>
    </div>
    <div class="page">PAGE <i>8</i></div>
  </article>

  <article class="slide" style="background:#fff">
    <svg class="abs" style="inset:0" width="244" height="137" viewBox="0 0 244 137">
      <polygon points="0,0 60,0 182,137 0,137" fill="var(--navy-2)"/>
    </svg>
    <div class="abs" style="left:16px;top:54px;color:#fff;font-family:Montserrat,sans-serif;font-weight:600;font-size:13px;line-height:1.2">FY – Define<br>Success</div>
    <span class="ic" style="left:63px;top:6px;width:20px;height:20px"><svg><use href="#i-target"/></svg></span><div class="abs" style="left:88px;top:13px;font-size:4px">Hit Growth Targets</div>
    <span class="ic" style="left:87px;top:31px;width:20px;height:20px"><svg><use href="#i-chart"/></svg></span><div class="abs" style="left:111px;top:38px;font-size:4px">Exceed Margin Guidance</div>
    <span class="ic" style="left:109px;top:56px;width:20px;height:20px"><svg><use href="#i-cycle"/></svg></span><div class="abs" style="left:138px;top:61px;font-size:4px;text-align:center">Consistency in Execution &amp;<br>Brilliant in the Basics</div>
    <span class="ic" style="left:133px;top:82px;width:20px;height:20px"><svg><use href="#i-eye"/></svg></span><div class="abs" style="left:164px;top:89px;font-size:4px">Vision and Plan set for Next Fiscal</div>
    <span class="ic" style="left:157px;top:108px;width:20px;height:20px"><svg><use href="#i-gear"/></svg></span><div class="abs" style="left:185px;top:116px;font-size:4px">Executive Relevance</div>
    <div class="page">PAGE <i>9</i></div>
  </article>

  <article class="slide">
    <div class="abs title" style="left:0;right:0;top:8px;text-align:center;font-size:13px;font-weight:500">Sponsors</div>
    <div class="abs" style="left:0;right:0;top:66px;height:62px;background:var(--blue)"></div>
    <div class="abs" style="left:13px;top:76px;width:220px;height:47px;background:var(--navy)"></div>
    <div class="abs" style="left:13px;top:36px;display:flex;gap:13px">
      <div role="img" aria-label="Sponsor portrait photograph" style="width:34px;height:40px;background:linear-gradient(180deg,#e6e2da,#c7b08a 55%,#8e8a88)"></div>
      <div role="img" aria-label="Sponsor portrait photograph" style="width:34px;height:40px;background:linear-gradient(180deg,#e8e4dc,#b69e86 55%,#6f6a70)"></div>
      <div role="img" aria-label="Sponsor portrait photograph" style="width:34px;height:40px;background:linear-gradient(180deg,#aeb9c6,#8f8c8c 55%,#3f4753)"></div>
      <div role="img" aria-label="Sponsor portrait photograph" style="width:34px;height:40px;background:linear-gradient(180deg,#7f8fa3,#a58b7c 55%,#232a36)"></div>
      <div role="img" aria-label="Sponsor portrait photograph" style="width:34px;height:40px;background:linear-gradient(180deg,#b8cde0,#c5a48e 55%,#4e5d70)"></div>
    </div>
    <div class="abs" style="left:13px;top:89px;display:flex;gap:13px;color:#fff;text-align:center">
      <div style="width:34px"><b style="font-size:4.2px">Mara Ellison</b><br><span style="font-size:2.8px">SVP Americas<br>Commercial<br>NORVEX</span></div>
      <div style="width:34px"><b style="font-size:4.2px">Tessa Rowan</b><br><span style="font-size:2.8px">VP<br>Global Services<br>NORVEX</span></div>
      <div style="width:34px"><b style="font-size:4.2px">Glen Ashby</b><br><span style="font-size:2.8px">AVP Americas<br>Commercial West<br>NORVEX</span></div>
      <div style="width:34px"><b style="font-size:4.2px">Reid Calloway</b><br><span style="font-size:2.8px">AVP Enterprise<br>Segment</span></div>
      <div style="width:34px"><b style="font-size:4.2px">Owen Pratt</b><br><span style="font-size:2.8px">CMO<br>CCI</span></div>
    </div>
    <div class="page">PAGE <i>10</i></div>
  </article>

  <article class="slide" style="background:var(--navy)">
    <div class="abs" style="inset:0;background:linear-gradient(135deg,#1a4688,#0c2e66 60%,#1b4a8a)" role="img" aria-label="Ocean wave photograph in navy tones"></div>
    <div class="abs" style="left:12px;top:18px;width:16px;height:16px;border:1.3px solid #fff;border-radius:50%;color:#fff;display:flex;align-items:center;justify-content:center"><svg width="8" height="8"><use href="#i-quote"/></svg></div>
    <div class="abs" style="left:35px;top:12px;color:var(--gold);font-family:Montserrat,sans-serif;font-weight:600;font-size:10px">Word of the Qtr: Kairos</div>
    <div class="abs" style="left:36px;top:26px;color:#fff;font-size:3.8px;width:175px">“a time when conditions are right for the accomplishment of a crucial action: the opportune and decisive moment”</div>
    <div class="abs" style="left:55px;top:44px;right:0;bottom:0;background:#fff;border-top-left-radius:10px"></div>
    <div class="abs" style="left:28px;top:70px;width:46px;height:46px;border-radius:50%;background:radial-gradient(circle,#fff 45%,var(--mist) 46%,var(--steel) 100%);border:3px solid var(--blue-2)" role="img" aria-label="Ride the Wave theme badge"></div>
    <div class="abs title" style="left:68px;top:52px;font-size:9px;font-weight:600">FY20 Theme:  Ride the Wave</div>
    <ul class="abs" style="left:80px;top:70px;list-style:none;font-size:3.7px;line-height:2.2">
      <li><svg width="4.5" height="4.5" style="vertical-align:-1px;color:var(--navy)"><use href="#i-arrow"/></svg> FY20 will begin with a <b>Wave</b> of significant <b>Change</b></li>
      <li><svg width="4.5" height="4.5" style="vertical-align:-1px;color:var(--navy)"><use href="#i-arrow"/></svg> Why this as a theme?  “From a Non-Surfer”</li>
      <li><svg width="4.5" height="4.5" style="vertical-align:-1px;color:var(--navy)"><use href="#i-arrow"/></svg> Tide matters, wind matters, wave conditions matter (external factors)</li>
      <li><svg width="4.5" height="4.5" style="vertical-align:-1px;color:var(--navy)"><use href="#i-arrow"/></svg> Takes a lot of work and energy to paddle out (you have to want it)</li>
      <li><svg width="4.5" height="4.5" style="vertical-align:-1px;color:var(--navy)"><use href="#i-arrow"/></svg> Lots of dangers(competitors) reef, rip tides, sharks, other surfers</li>
      <li><svg width="4.5" height="4.5" style="vertical-align:-1px;color:var(--navy)"><use href="#i-arrow"/></svg> Right wave, right height, go with the wave, lean into it, enjoy the ride.</li>
    </ul>
  </article>

  <article class="slide">
    <div class="abs title" style="left:12px;top:6px;font-size:8.5px">Select “Excellence in Role or The Gold Standard”</div>
    <div class="tag" style="left:8px;top:24px;background:var(--blue)">TRAINING &amp; DEVELOPMENT</div>
    <ul class="abs bullets" style="left:12px;top:33px;width:82px;font-size:2.6px;color:var(--grey)"><li>Aligned to forecast confidence guidelines</li><li>Leveraging account plan template and heatmap</li><li>Completes mandated corporate and SP training</li><li>Contributes and makes an impact beyond role</li><li>Leverage the ROD SE Lab</li></ul>
    <div class="tag" style="left:160px;top:24px;background:var(--sky)">OPERATIONAL EXCELLENCE</div>
    <ul class="abs bullets" style="left:160px;top:33px;width:80px;font-size:2.6px;color:var(--grey)"><li>Stretch vs. Hero forecasting: 70% commit w risk</li><li>Thorough deal assurance knowledge</li><li>Comprehensive territory plans with Qtrly milestones</li><li>No past due opportunities</li><li>All opportunities have technology and SE assigned</li><li>Leverage GFEP for Post-Sales Support</li></ul>
    <div class="tag" style="left:8px;top:74px;background:var(--blue-2);width:75px">GTM</div>
    <ul class="abs bullets" style="left:12px;top:82px;width:80px;font-size:2.6px;color:var(--grey)"><li>Leverage the power of ONE team</li><li>Planning and regular cadence with extended team and virtual sales</li><li>Scale through partners</li><li>Leverage programs to build pipeline</li></ul>
    <div class="tag" style="left:158px;top:82px;background:var(--navy)">ARCHITECTURES &amp; SOLUTIONS</div>
    <ul class="abs bullets" style="left:162px;top:91px;width:78px;font-size:2.6px;color:var(--grey)"><li>Utilize account data and knowledge of customer business models</li><li>Protect the base, aggressively pursue renewals</li><li>Builds migration path to solutions vs boxes</li><li>Leverage channel and extended team to sell</li><li>Utilize heat map across accounts</li></ul>
    <svg class="abs" style="left:91px;top:36px" width="70" height="70" viewBox="0 0 70 70">
      <circle cx="35" cy="35" r="29" fill="none" stroke="var(--sky)" stroke-width="8" stroke-dasharray="45 137" transform="rotate(-90 35 35)"/>
      <circle cx="35" cy="35" r="29" fill="none" stroke="var(--blue)" stroke-width="8" stroke-dasharray="45 137" transform="rotate(180 35 35)"/>
      <circle cx="35" cy="35" r="29" fill="none" stroke="var(--blue-2)" stroke-width="8" stroke-dasharray="45 137" transform="rotate(90 35 35)"/>
      <circle cx="35" cy="35" r="29" fill="none" stroke="var(--navy)" stroke-width="8" stroke-dasharray="45 137"/>
      <polygon points="35,14 53,24 53,46 35,56 17,46 17,24" fill="#fff" stroke="var(--navy)" stroke-width="2"/>
    </svg>
    <div class="abs" style="left:110px;top:61px;width:32px;text-align:center;font-size:4px;font-weight:700;color:var(--navy);line-height:1.15">Excellence in Role or The Gold Standard</div>
    <div class="page">PAGE <i>11</i></div>
  </article>

  <article class="slide">
    <ul class="abs bullets" style="left:8px;top:16px;width:78px;font-size:2.6px;color:var(--grey)"><li>Utilize account data and knowledge of customer business models</li><li>Protect the base, aggressively pursue renewals</li><li>Builds migration path to solutions vs boxes</li><li>Leverage channel and extended team to sell</li><li>Utilize heat map across accounts</li></ul>
    <ul class="abs bullets" style="left:160px;top:10px;width:80px;font-size:2.6px;color:var(--grey)"><li>Stretch vs. Hero forecasting: 70% commit w risk</li><li>Thorough deal assurance knowledge</li><li>Comprehensive territory plans with Qtrly milestones</li><li>No past due opportunities</li><li>All opportunities have technology and SE assigned</li><li>Leverage GFEP for Post-Sales Support</li></ul>
    <div class="tag" style="left:0;top:59px;width:98px;background:var(--navy);font-size:3.8px">ARCHITECTURES &amp; SOLUTIONS</div>
    <div class="tag" style="left:0;top:71px;width:98px;background:var(--blue-2);font-size:3.8px">GTM</div>
    <div class="tag" style="left:146px;top:59px;width:98px;background:var(--sky);font-size:3.8px;padding-left:20px">OPERATIONAL EXCELLENCE</div>
    <div class="tag" style="left:146px;top:71px;width:98px;background:var(--blue);font-size:3.8px;padding-left:20px">TRAINING &amp; DEVELOPMENT</div>
    <ul class="abs bullets" style="left:10px;top:84px;width:80px;font-size:2.6px;color:var(--grey)"><li>Leverage the power of ONE team</li><li>Planning and regular cadence with extended team and virtual sales</li><li>Scale through partners</li><li>Leverage programs to build pipeline</li></ul>
    <ul class="abs bullets" style="left:166px;top:84px;width:74px;font-size:2.6px;color:var(--grey)"><li>Aligned to forecast confidence guidelines</li><li>Leveraging account plan template and heatmap</li><li>Completes mandated corporate and SP training</li><li>Contributes and makes an impact beyond role</li><li>Leverage the ROD SE Lab</li></ul>
    <svg class="abs" style="left:88px;top:30px" width="68" height="84" viewBox="0 0 68 84">
      <circle cx="34" cy="42" r="30" fill="#fff" stroke="var(--mist)" stroke-width="7"/>
      <path d="M34 12 A30 30 0 0 0 4 42" fill="none" stroke="var(--navy)" stroke-width="7"/>
      <path d="M64 42 A30 30 0 0 0 34 12" fill="none" stroke="var(--sky)" stroke-width="7"/>
      <path d="M4 42 A30 30 0 0 0 34 72" fill="none" stroke="var(--blue-2)" stroke-width="7"/>
      <path d="M34 72 A30 30 0 0 0 64 42" fill="none" stroke="var(--blue)" stroke-width="7"/>
    </svg>
    <div class="abs" style="left:100px;top:55px;width:44px;text-align:center;font-size:5px;color:var(--navy);font-weight:600;line-height:1.2">Select<br><span style="color:var(--gold);font-size:4.4px">“Excellence in Role or The Gold Standard”</span></div>
    <div class="page">PAGE <i>12</i></div>
  </article>

  <article class="slide" style="background:linear-gradient(180deg,#fff,#f1f4f8)">
    <div class="abs title" style="left:0;right:0;top:10px;text-align:center;font-size:10px;font-weight:500">Leadership Expectations–Sales Leaders</div>
    <div class="exp-card" style="left:18px;top:38px;width:62px;height:82px;padding:14px 4px 0 5px">
      <div class="rule"></div><div class="num" style="right:6px;top:-7px">01.</div>
      <b style="font-size:4.3px;color:var(--navy)">Be a Culture Builder</b>
      <ul class="bullets" style="margin-top:8px;font-size:3px;line-height:1.4"><li>Personal Humility and Professional Will (be a role model)</li><li>Engage others in shared meaning</li><li>Scale through influence</li></ul>
    </div>
    <div class="exp-card" style="left:89px;top:38px;width:62px;height:82px;padding:10px 4px 0 5px">
      <div class="rule"></div><div class="num" style="right:6px;top:-7px">02.</div>
      <b style="font-size:4.3px;color:var(--navy)">Own the Number and the Details</b>
      <ul class="bullets" style="margin-top:5px;font-size:3px;line-height:1.4"><li>Demonstrate sustainable value to our customers, partners and team</li><li>Timely communication | Limit surprises | High Care Factor</li><li>Know our business | Ensure each IC knows the business</li></ul>
    </div>
    <div class="exp-card" style="left:160px;top:38px;width:62px;height:82px;padding:10px 4px 0 5px">
      <div class="rule"></div><div class="num" style="right:6px;top:-7px">03.</div>
      <b style="font-size:4.3px;color:var(--navy)">Contribute Beyond Region Objectives</b>
      <ul class="bullets" style="margin-top:5px;font-size:3px;line-height:1.4"><li>Be part of the solution</li><li>Share a better idea (better to light a candle than curse the darkness)</li><li>Make each other successful</li></ul>
    </div>
    <div class="page">PAGE <i>14</i></div>
  </article>

  <article class="slide" style="background:linear-gradient(180deg,#fff,#f1f4f8)">
    <div class="abs title" style="left:0;right:0;top:12px;text-align:center;font-size:10px;font-weight:500">Leadership Expectations–Sales Leaders</div>
    <div class="exp-card" style="left:38px;top:40px;width:76px;height:78px;padding:14px 5px 0 6px">
      <div class="rule" style="width:22px"></div><div class="num" style="right:8px;top:-7px">01.</div>
      <b style="display:block;text-align:center;font-size:4.5px;color:var(--navy)">Grow in Role</b>
      <ul class="bullets" style="margin-top:6px;font-size:3.5px;line-height:1.35"><li>If you aren’t learning you aren’t moving forward</li><li>Positively influence the learning of others</li><li>What’s next discussion bi-annually? (own your development plan)</li></ul>
    </div>
    <div class="exp-card" style="left:122px;top:40px;width:80px;height:78px;padding:14px 5px 0 6px">
      <div class="rule" style="width:22px"></div><div class="num" style="right:8px;top:-7px">02.</div>
      <b style="display:block;text-align:center;font-size:4.5px;color:var(--navy)">Live by the Golden Rule</b>
      <ul class="bullets" style="margin-top:6px;font-size:3.5px;line-height:1.35"><li>Don’t tolerate intolerable behavior</li><li>Don’t let people waste other people’s time</li><li>Say Thank-you often</li></ul>
    </div>
    <div class="page">PAGE <i>15</i></div>
  </article>

  <article class="slide">
    <div class="abs title" style="left:0;right:0;top:6px;text-align:center;font-size:10px;font-weight:500">Career: Timeline</div>
    <svg class="abs" style="inset:0" width="244" height="137" viewBox="0 0 244 137">
      <path d="M42 42 L212 42 M42 42 Q12 42 12 70 Q12 97 42 97 L212 97 Q224 97 220 137" fill="none" stroke="#c4ccd6" stroke-width=".8" stroke-dasharray="1.5 1.5"/>
    </svg>
    <div class="abs" style="left:33px;top:21px;font-size:4px;font-weight:700;color:var(--blue-2)">■ NORVEX</div>
    <div class="abs" style="left:200px;top:19px;width:24px;height:24px;border-radius:50%;background:var(--gold);color:var(--navy);font-size:5px;font-weight:700;text-align:center;line-height:24px;box-shadow:0 0 0 2px var(--cream)">2020</div>
    <div class="abs" style="left:189px;top:46px;background:var(--blue);color:#fff;font-size:4px;padding:1px 3px">Add your Text Here</div>
    <div class="year" style="left:33px;top:33px">2014</div>
    <div class="cap" style="left:20px;top:54px;width:44px">Regional Manager, Southwest Territory Regional Manager, Metro Select</div>
    <div class="year" style="left:88px;top:33px">2017</div>
    <div class="cap" style="left:75px;top:54px;width:44px">Operations Director, Service Provider US</div>
    <div class="year" style="left:136px;top:33px">2019</div>
    <div class="cap" style="left:123px;top:54px;width:44px">Operations Director, Mid Markets Select</div>
    <div class="abs" style="left:44px;top:80px;font-size:4px;color:var(--ink)">Quillfield</div>
    <div class="abs" style="left:104px;top:80px;font-size:4px;color:var(--ink)">Stafforge</div>
    <div class="abs" style="left:167px;top:72px;width:14px;height:14px;border-radius:50%;background:#8a2b2b;box-shadow:0 0 0 1.5px var(--gold)"></div>
    <div class="year" style="left:45px;top:88px">2004</div>
    <div class="cap" style="left:32px;top:109px;width:44px">Inside Sales Manager, Outside Sales Manager, General Manager</div>
    <div class="year" style="left:106px;top:88px">1999</div>
    <div class="cap" style="left:89px;top:109px;width:52px">Account Manager, Branch Manager and Area Director</div>
    <div class="year" style="left:165px;top:88px">1993</div>
    <div class="cap" style="left:152px;top:109px;width:44px">Officer, Reserve Corps</div>
    <div class="page">PAGE <i>16</i></div>
  </article>

  <article class="slide">
    <div class="abs" style="left:0;top:0;width:120px;bottom:0;background:radial-gradient(circle at 40% 40%,#24508f,#0a2350 75%)" role="img" aria-label="Dark blue starry sky photograph"></div>
    <div class="abs" style="left:120px;top:0;right:0;bottom:0;background:#f4f6f9"></div>
    <svg class="abs" style="left:83px;top:28px" width="78" height="82" viewBox="0 0 78 82">
      <path d="M39 2 Q43 2 47 4 L72 19 Q76 21 76 26 L76 56 Q76 61 72 63 L47 78 Q43 80 39 80 Q35 80 31 78 L6 63 Q2 61 2 56 L2 26 Q2 21 6 19 L31 4 Q35 2 39 2Z" fill="#1a9be0"/>
    </svg>
    <div class="abs" style="left:83px;top:60px;width:78px;text-align:center;color:#fff;font-family:Montserrat,sans-serif;font-weight:600;font-size:12px">Appendix</div>
    <div class="page">PAGE <i>18</i></div>
  </article>

  <article class="slide">
    <div class="abs" style="inset:0;background:radial-gradient(ellipse at 30% 40%,#3f6fa8,#1c3f73 55%,#10284f)" role="img" aria-label="Blue toned technology photograph with rising line graph"></div>
    <div class="abs" style="left:10px;top:121px;width:136px;height:.7px;background:#fff"></div>
    <div class="abs" style="right:8px;top:109px;color:#fff;font-family:Montserrat,sans-serif;font-weight:700;font-size:17px;line-height:1">Thank you</div>
  </article>

</main>
</body>
</html>
```